Local fast-growing company in the service sector

We are looking for a modern business card design, which should also appear on our letterheads

Target Market(s)

Private and industrial sectors

Contact Information for Business Card

Vorname Name
Lindkofer Str. 18
71468 Lindenbrück
Tel.: 07163-418259-0
Name@kovaltec-pbz.de

Colors
9d9d9d
919191
aaaaaa

Requirements
Must have
• The logo (file) in silver

```html
<!DOCTYPE html>
<html lang="de">
<head>
<meta charset="utf-8">
<title>Visitenkarte – Kovaltec</title>
<link rel="stylesheet" href="https://fonts.googleapis.com/css2?family=Michroma&family=Quicksand:wght@500;600&display=swap">
<style>
  :root {
    --page-bg: #d9d4cc;
    --card-bg: #3a3938;
    --card-edge: #8f8d8a;
    --silver: #aaaaaa;
    --name-gold: #d6c7ad;
    --text-light: #d9d3c7;
  }
  * { margin: 0; padding: 0; box-sizing: border-box; }
  html, body {
    width: 1200px;
    height: 1010px;
    overflow: hidden;
    background: var(--page-bg);
  }
  .canvas {
    position: relative;
    width: 1200px;
    height: 1010px;
  }
  .business-card {
    position: absolute;
    left: 174px;
    top: 281px;
    width: 852px;
    height: 495px;
    background: linear-gradient(160deg, #444341 0%, var(--card-bg) 55%, #343332 100%);
    border: 1px solid var(--card-edge);
  }
  .brand {
    position: absolute;
    left: 100px;
    top: 217px;
    display: flex;
    align-items: center;
    gap: 14px;
    font-family: "Quicksand", sans-serif;
    font-weight: 600;
    font-size: 42px;
    color: var(--silver);
    letter-spacing: 1px;
  }
  .brand-square {
    width: 22px;
    height: 22px;
    background: var(--silver);
  }
  .contact {
    position: absolute;
    left: 423px;
    top: 158px;
  }
  .contact-name {
    font-family: "Michroma", sans-serif;
    font-weight: 400;
    font-size: 23px;
    letter-spacing: 2px;
    color: var(--name-gold);
    margin-bottom: 22px;
  }
  .contact-line {
    font-family: "Quicksand", sans-serif;
    font-weight: 500;
    font-size: 19px;
    line-height: 29px;
    color: var(--text-light);
    letter-spacing: 0.5px;
    padding-left: 8px;
  }
  .contact-line.with-icon {
    display: flex;
    align-items: center;
    gap: 22px;
  }
  .contact-line.with-icon svg {
    width: 18px;
    height: 14px;
    fill: var(--text-light);
  }
</style>
</head>
<body>
  <main class="canvas">
    <section class="business-card">
      <div class="brand">
        <span class="brand-square"></span>
        <span class="brand-name">Kovaltec</span>
      </div>

      <div class="contact">
        <h1 class="contact-name">VORNAME NAME</h1>
        <p class="contact-line">Lindkofer Str. 18</p>
        <p class="contact-line">71468 Lindenbrück</p>
        <p class="contact-line with-icon">
          <svg viewBox="0 0 18 14" aria-hidden="true">
            <path d="M1 4 Q9 -1 17 4 L15 6 L12 4.5 L12 3 Q9 2 6 3 L6 4.5 L3 6 Z"/>
            <rect x="4" y="7" width="10" height="7" rx="1"/>
          </svg>
          <span>07163-418259-0</span>
        </p>
        <p class="contact-line with-icon">
          <svg viewBox="0 0 18 14" aria-hidden="true">
            <path d="M1 2 H17 V13 H1 Z M2.5 3 L9 8 L15.5 3 Z" fill-rule="evenodd"/>
          </svg>
          <span>name@kovaltec-pbz.de</span>
        </p>
      </div>
    </section>
  </main>
</body>
</html>
```